Plumquill.media

I need a full page PSD made (desktop and mobile view) with a layout similar to what I have in my text file, but a smooth flowing, good looking design. Only take my text file as an idea of order things show flow. I have taken my exact steps from the text file, put them together, and it did not look good, which is why I am seeking a professional design.

```html
<!DOCTYPE html>
<html lang="en">
<head>
<meta charset="utf-8">
<title>Plumquill.media — Reviews and Text Marketing</title>
<link href="https://fonts.googleapis.com/css2?family=Raleway:wght@400;500;600;700;800&family=Montserrat:wght@700;800;900&family=Roboto:wght@400;500&display=swap" rel="stylesheet">
<style>
:root{
  --red:#e1001f;
  --red-dark:#c4162f;
  --teal:#0e5c78;
  --blue:#1358a4;
  --blue-card:#1456a3;
  --blue-light:#88acd3;
  --ink:#2f2f2f;
  --white:#ffffff;
  --bubble:#e7e7ec;
  --bubble-blue:#7fa8f0;
}
*{margin:0;padding:0;box-sizing:border-box}
html,body{width:1200px;height:3000px;overflow:hidden;background:var(--white)}
body{position:relative;font-family:'Raleway',sans-serif;color:var(--ink)}
.abs{position:absolute}

/* header */
.brand{left:186px;top:38px;font-family:'Raleway',sans-serif;font-weight:700;font-size:38px;color:#333;letter-spacing:-0.5px}
.nav{top:68px;font-size:13px;font-weight:500;color:#222;letter-spacing:.3px}
.top-band{left:0;top:122px;width:1200px;height:42px;background:var(--red)}

/* hero */
.hero{left:0;top:164px;width:1200px;height:526px;background:linear-gradient(100deg,#3f5682 0%,#2f4674 40%,#4d6590 70%,#6a7fa3 100%)}
.hero-title{left:150px;top:244px;font-family:'Montserrat',sans-serif;font-weight:800;font-size:45px;line-height:54px;color:var(--white);text-transform:uppercase}
.hero-sub{left:150px;top:456px;font-family:'Montserrat',sans-serif;font-weight:700;font-size:26px;color:var(--white)}
.btn{background:var(--red-dark);color:var(--white);font-size:13px;display:flex;align-items:center;justify-content:center;border-radius:2px}
.hero-btn{left:150px;top:549px;width:149px;height:37px}
.quote-who{left:750px;top:311px;width:299px;height:112px;background:var(--red);border-radius:40px}
.avatar{left:783px;top:329px;width:76px;height:76px;border-radius:50%;background:linear-gradient(135deg,#8a6a55,#c9a48c)}
.who-name{left:891px;top:345px;font-family:'Montserrat',sans-serif;font-weight:800;font-size:15px;color:var(--white)}
.who-co{left:891px;top:372px;font-size:11px;color:var(--white)}
.quote-text{left:750px;top:435px;width:299px;height:111px;background:rgba(255,255,255,.9);border-radius:36px}
.quote-mark{left:796px;top:440px;font-size:28px;font-weight:700;color:#444}
.quote-body{left:812px;top:470px;font-size:18px;line-height:22px;color:#555}

/* section headings */
.sec-title{left:0;width:1200px;text-align:center;font-weight:700;font-size:46px;color:var(--teal)}
.sec-sub{left:0;width:1200px;text-align:center;font-weight:500;font-size:22px;color:var(--teal)}

/* review grid */
.grid{left:153px;top:846px;width:897px;height:750px;background:var(--red)}
.photo-sign{left:153px;top:846px;width:499px;height:299px;background:linear-gradient(90deg,#4a3a30 0%,#6d5a48 35%,#d8d8d6 45%,#efefed 70%,#5a4a3e 100%)}
.step-label{font-size:22px;font-weight:500;color:var(--white)}
.step-text{font-size:24px;font-weight:600;line-height:30px;color:var(--white)}
.bubble{background:var(--bubble);border-radius:14px;font-family:'Roboto',sans-serif;font-size:10px;line-height:12px;color:#222;padding:12px 12px}
.bubble-me{background:var(--bubble-blue);border-radius:8px;font-family:'Roboto',sans-serif;font-size:10px;color:#222;display:flex;align-items:center;padding-left:10px}
.link{color:#1a4fd0;text-decoration:underline}
.white-panel{left:662px;top:1154px;width:380px;height:434px;background:var(--white)}
.shot{left:721px;top:1169px;width:271px;height:276px;background:linear-gradient(180deg,#8fb0ee 0%,#8fb0ee 22%,#f2f2f2 22%,#f2f2f2 100%)}
.step-red{color:var(--red)}

/* text marketing */
.tm-band{left:0;top:1745px;width:1200px;height:416px;background:var(--blue)}
.tm-text{left:150px;top:1770px;width:430px;font-weight:500;font-size:23px;line-height:36px;color:var(--white);text-transform:uppercase}
.tm-text p{margin-bottom:36px}
.phone-photo{left:600px;top:1773px;width:450px;height:359px;background:linear-gradient(120deg,#dfe6ee 0%,#f1f3f6 45%,#b98e74 75%,#d3a88b 100%)}

/* pricing */
.price-band{left:0;top:2307px;width:1200px;height:451px;background:var(--blue-light)}
.price-card{left:485px;top:2345px;width:262px;height:374px;background:var(--blue-card)}
.price{left:485px;top:2362px;width:262px;text-align:center;color:var(--white)}
.price .cur{font-size:40px;font-weight:400;vertical-align:6px}
.price .amt{font-family:'Montserrat',sans-serif;font-weight:900;font-size:50px}
.price .per{font-family:'Montserrat',sans-serif;font-weight:800;font-size:13px}
.features{left:502px;top:2462px;list-style:none}
.features li{display:flex;align-items:center;height:36px;font-size:13.5px;font-weight:500;color:var(--white);text-transform:uppercase}
.features svg{margin-right:10px}
.select-btn{left:539px;top:2656px;width:151px;height:36px}

/* footer */
.foot-brand{left:0;width:1200px;top:2838px;text-align:center;font-weight:700;font-size:30px;color:#333}
.foot-call{left:0;width:1200px;top:2910px;text-align:center;font-size:11px;line-height:13px;color:#333}
.foot-rule{left:150px;top:2959px;width:900px;height:1px;background:#999}
.foot-copy{left:0;width:1200px;top:2976px;text-align:center;font-size:9px;color:#333}
</style>
</head>
<body>

<header>
  <div class="abs brand">Plumquill.media</div>
  <nav>
    <span class="abs nav" style="left:697px">HOME</span>
    <span class="abs nav" style="left:769px">PRICING</span>
    <span class="abs nav" style="left:853px">CONTACT</span>
    <span class="abs nav" style="left:945px">LOGIN</span>
  </nav>
</header>
<div class="abs top-band"></div>

<section>
  <div class="abs hero" role="img" aria-label="Cashier at a store counter using a point of sale terminal, with a blue overlay"></div>
  <h1 class="abs hero-title">Get 5 star reviews<br>and text message<br>marketing</h1>
  <div class="abs hero-sub">ALL IN ONE TOOL!</div>
  <div class="abs btn hero-btn">LEARN MORE</div>

  <div class="abs quote-who"></div>
  <div class="abs avatar" role="img" aria-label="Customer portrait"></div>
  <div class="abs who-name">DANA REYES</div>
  <div class="abs who-co">BRIGHTSIDE GOODS CO.</div>
  <div class="abs quote-text"></div>
  <div class="abs quote-mark">&ldquo;</div>
  <div class="abs quote-body">Would recommend to<br>friends and family.</div>
</section>

<section>
  <h2 class="abs sec-title" style="top:732px">HOW IT WORKS</h2>
  <div class="abs sec-sub" style="top:790px">5 STAR REVIEW SYSTEM</div>

  <div class="abs grid"></div>
  <div class="abs photo-sign" role="img" aria-label="Paper sign by a cafe register offering 50% off for texting a short code"></div>
  <div class="abs step-label" style="left:701px;top:917px">Step 1</div>
  <div class="abs step-text" style="left:701px;top:975px;width:330px">You display an offer near your cash register.</div>

  <div class="abs bubble" style="left:170px;top:1198px;width:244px;height:110px">Thank you for being a valued customer.<br>This will only take a minute!<br><br>One a scale of 1 to 5, how many stars would you rate our establishment?<br><br>Please reply with a number.</div>
  <div class="abs bubble-me" style="left:310px;top:1315px;width:104px;height:24px">5</div>
  <div class="abs bubble" style="left:170px;top:1346px;width:244px;height:108px">Thank you! Can you take 1 minute to leave us a review on the Searchly link below?<br><br><span class="link">http://www.searchly.com/StoreLink</span><br><br>When you are finished, please reply with the word "Done" to receive your 50% off.</div>
  <div class="abs bubble-me" style="left:310px;top:1464px;width:104px;height:24px">Done</div>
  <div class="abs bubble" style="left:170px;top:1496px;width:244px;height:48px">You're Awsome! Please show this message to the cashier and mention the discount.</div>

  <div class="abs step-label" style="left:433px;top:1200px">Step 2</div>
  <div class="abs step-text" style="left:433px;top:1257px;width:225px">Customer starts the review sequence. Only 5 star responses are directed to your search link. 1-4 star responses are asked to reply with feedback.</div>

  <div class="abs white-panel"></div>
  <div class="abs shot" role="img" aria-label="Business listing notification showing a new 5-star review"></div>
  <div class="abs step-label step-red" style="left:726px;top:1460px">Step 3</div>
  <div class="abs step-text step-red" style="left:726px;top:1517px;width:300px">Your business earns 5 star reviews!</div>
</section>

<section>
  <h2 class="abs sec-title" style="top:1636px">HOW IT WORKS</h2>
  <div class="abs sec-sub" style="top:1693px">TEXT MARKETING SYSTEM</div>
  <div class="abs tm-band"></div>
  <div class="abs tm-text">
    <p>1. Phone numbers are collected from cash register offer.</p>
    <p>2. Simply log into the dashboard and send all your customers a text message of any specials or promotions.</p>
    <p>3. Watch your customer come through the door!</p>
  </div>
  <div class="abs phone-photo" role="img" aria-label="Hand holding a phone showing a text message about a buy one get one donut special"></div>
</section>

<section>
  <h2 class="abs sec-title" style="top:2200px;font-size:46px">PRICING</h2>
  <div class="abs sec-sub" style="top:2262px">SIMPLE PRICE. ALL THE BENEFITS</div>
  <div class="abs price-band"></div>
  <div class="abs price-card"></div>
  <div class="abs price"><span class="cur">$ </span><span class="amt">149</span> <span class="per">/mo</span></div>
  <ul class="abs features">
    <li><svg width="22" height="20" viewBox="0 0 22 20"><rect x="1" y="3" width="15" height="15" fill="none" stroke="#fff" stroke-width="1.6"/><path d="M4 10l4 4 12-13" fill="none" stroke="#fff" stroke-width="2"/></svg>Customer review system</li>
    <li><svg width="22" height="20" viewBox="0 0 22 20"><rect x="1" y="3" width="15" height="15" fill="none" stroke="#fff" stroke-width="1.6"/><path d="M4 10l4 4 12-13" fill="none" stroke="#fff" stroke-width="2"/></svg>Text message marketing</li>
    <li><svg width="22" height="20" viewBox="0 0 22 20"><rect x="1" y="3" width="15" height="15" fill="none" stroke="#fff" stroke-width="1.6"/><path d="M4 10l4 4 12-13" fill="none" stroke="#fff" stroke-width="2"/></svg>Customer feedback</li>
    <li><svg width="22" height="20" viewBox="0 0 22 20"><rect x="1" y="3" width="15" height="15" fill="none" stroke="#fff" stroke-width="1.6"/><path d="M4 10l4 4 12-13" fill="none" stroke="#fff" stroke-width="2"/></svg>Email notifications</li>
    <li><svg width="22" height="20" viewBox="0 0 22 20"><rect x="1" y="3" width="15" height="15" fill="none" stroke="#fff" stroke-width="1.6"/><path d="M4 10l4 4 12-13" fill="none" stroke="#fff" stroke-width="2"/></svg>Online dashboard</li>
  </ul>
  <div class="abs btn select-btn">Select</div>
</section>

<footer>
  <div class="abs foot-brand">Plumquill.media</div>
  <div class="abs foot-call">Call us:<br>(555) xxx - xxxx</div>
  <div class="abs foot-rule"></div>
  <div class="abs foot-copy">&copy;plumquill.media</div>
</footer>

</body>
</html>
```